Need DL Flyer for Real Estate Drops

We need a real estate flyer ,double sided. With content on 1 side like: Want to know what's your house is worth " contact us today and on other side agent details. We are looking for an ongoing partnership with designer so this assignment will be ongoing

```html
<!DOCTYPE html>
<html lang="en">
<head>
<meta charset="utf-8">
<title>Dunewood Real Estate – DL Flyer</title>
<link rel="stylesheet" href="https://fonts.googleapis.com/css2?family=Fira+Sans:wght@400;500;600;700&display=swap">
<style>
  :root {
    --brand-red: #c62128;
    --brand-navy: #13183f;
    --white: #ffffff;
    --backdrop: #dcdcdc;
    --text-dark: #16182e;
  }
  * { box-sizing: border-box; margin: 0; padding: 0; }
  html, body { width: 1200px; height: 1200px; overflow: hidden; }
  body {
    background: var(--backdrop);
    font-family: "Fira Sans", sans-serif;
    position: relative;
  }
  .flyer {
    position: absolute;
    top: 150px;
    width: 450px;
    height: 900px;
    background: var(--white);
    overflow: hidden;
  }
  .flyer--front { left: 117px; }
  .flyer--back { left: 633px; }

  /* Wordmark */
  .wordmark {
    position: absolute;
    top: 72px;
    left: 0;
    width: 100%;
    display: flex;
    align-items: center;
    justify-content: center;
    gap: 16px;
  }
  .wordmark__square { width: 52px; height: 52px; }
  .wordmark__name {
    font-weight: 600;
    font-size: 34px;
    letter-spacing: 0.2px;
    white-space: nowrap;
  }
  .flyer--front .wordmark__square { background: var(--brand-red); }
  .flyer--front .wordmark__name { color: var(--brand-navy); }
  .flyer--back .wordmark__square { background: var(--brand-navy); }
  .flyer--back .wordmark__name { color: var(--white); }

  /* Front side */
  .front__red-band {
    position: absolute;
    left: 0; top: 470px;
    width: 450px; height: 291px;
    background: var(--brand-red);
    border-bottom-left-radius: 72px;
  }
  .front__photo {
    position: absolute;
    left: 0; top: 195px;
    width: 450px; height: 357px;
    border-top-left-radius: 80px;
    border-bottom-right-radius: 80px;
    background: linear-gradient(160deg, #ededed 0%, #dcdcdc 45%, #b9bfc8 75%, #8e97a3 100%);
  }
  .front__headline {
    position: absolute;
    left: 59px; top: 576px;
    color: var(--white);
    font-weight: 700;
    line-height: 1;
  }
  .front__headline .line-lg { display: block; font-size: 46px; }
  .front__headline .line-sm { display: block; font-size: 31px; margin: 8px 0 6px 32px; font-weight: 600; }
  .front__cta {
    position: absolute;
    left: 65px; top: 734px;
    width: 320px; height: 50px;
    border-radius: 25px;
    background: var(--brand-navy);
    border: 2px solid var(--white);
    color: var(--white);
    font-weight: 700;
    font-size: 26px;
    display: flex; align-items: center; justify-content: center;
    letter-spacing: 0.3px;
  }
  .front__phone {
    position: absolute;
    left: 0; top: 794px;
    width: 100%;
    display: flex; align-items: center; justify-content: center;
    gap: 6px;
    color: var(--brand-red);
    font-weight: 700;
    font-size: 42px;
    line-height: 1;
  }
  .front__phone svg { width: 36px; height: 36px; }
  .front__web {
    position: absolute;
    left: 0; top: 848px;
    width: 100%;
    text-align: center;
    font-weight: 600;
    font-size: 20px;
    color: var(--text-dark);
  }
  .front__web .accent { color: var(--brand-red); }
  .front__web .navy { color: var(--brand-navy); }

  /* Back side */
  .back__photo {
    position: absolute;
    left: 0; top: 150px;
    width: 450px; height: 380px;
    background: linear-gradient(180deg, #f1f1ef 0%, #e4e3df 40%, #cfcac2 70%, #8a6b4f 100%);
  }
  .back__header {
    position: absolute;
    left: 0; top: 0;
    width: 450px; height: 193px;
    background: var(--brand-red);
    border-bottom-left-radius: 92px;
  }
  .back__contact-panel {
    position: absolute;
    left: 0; top: 449px;
    width: 450px; height: 269px;
    background: var(--brand-red);
    border-top-right-radius: 92px;
    border-bottom-left-radius: 92px;
  }
  .back__agent-photo {
    position: absolute;
    left: 147px; top: 368px;
    width: 156px; height: 156px;
    border-radius: 50%;
    border: 6px solid var(--brand-red);
    background: linear-gradient(180deg, #eef0f2 0%, #dfe3e8 60%, #f7f7f7 100%);
  }
  .back__agent-name {
    position: absolute;
    left: 0; top: 532px;
    width: 100%;
    text-align: center;
    color: var(--white);
    font-weight: 600;
    font-size: 32px;
  }
  .back__rule {
    position: absolute;
    left: 46px; width: 358px; height: 1.5px;
    background: var(--white);
  }
  .back__rule--top { top: 580px; }
  .back__rule--bottom { top: 645px; }
  .back__phone {
    position: absolute;
    left: 0; top: 590px;
    width: 100%;
    display: flex; align-items: center; justify-content: center;
    gap: 8px;
    color: var(--white);
    font-weight: 700;
    font-size: 42px;
    line-height: 1;
  }
  .back__phone svg { width: 36px; height: 36px; }
  .back__online {
    position: absolute;
    left: 0; top: 656px;
    width: 100%;
    text-align: center;
    color: var(--white);
    font-size: 16px;
    line-height: 25px;
  }
  .back__divider {
    position: absolute;
    top: 733px; left: 78px;
    width: 294px; height: 18px;
  }
  .office {
    position: absolute;
    left: 0; width: 100%;
    text-align: center;
    line-height: 21px;
  }
  .office--head { top: 759px; }
  .office--branch { top: 821px; }
  .office__label { color: var(--brand-red); font-weight: 600; font-size: 16px; }
  .office__address { color: var(--brand-navy); font-weight: 500; font-size: 16px; }
</style>
</head>
<body>

<section class="flyer flyer--front" aria-label="Flyer front">
  <div class="wordmark">
    <span class="wordmark__square"></span>
    <span class="wordmark__name">Dunewood Real Estate</span>
  </div>

  <div class="front__red-band"></div>
  <div class="front__photo" role="img" aria-label="Photo of a smiling young family sitting on the floor among moving boxes, holding a cardboard roof over their heads"></div>

  <h1 class="front__headline">
    <span class="line-lg">Want to know</span>
    <span class="line-sm">what's your</span>
    <span class="line-lg">house is worth</span>
  </h1>

  <div class="front__cta">CONTACT US TODAY</div>

  <div class="front__phone">
    <svg viewBox="0 0 40 40" aria-hidden="true">
      <circle cx="20" cy="20" r="17" fill="none" stroke="currentColor" stroke-width="3"/>
      <path d="M14 11c1-1 2.5-1 3 0l2 4c.4.9 0 1.8-.8 2.3l-1.3.8c.9 2.3 2.6 4.2 4.8 5.3l.9-1.2c.6-.8 1.5-1 2.3-.6l3.8 2.1c.9.5 1 1.9.1 2.8l-1.4 1.4c-1.3 1.3-3.3 1.6-5 .8-4.6-2.2-8.1-5.9-10-10.6-.7-1.7-.3-3.6 1-4.9z" fill="currentColor"/>
    </svg>
    <span>03 9012 4470</span>
  </div>

  <p class="front__web">www.<span class="accent">Dunewood</span><span class="navy">RealEstate</span>.com.au</p>
</section>

<section class="flyer flyer--back" aria-label="Flyer back">
  <div class="back__photo" role="img" aria-label="Photo of a bright modern kitchen with white island bench and large windows"></div>
  <div class="back__header"></div>
  <div class="wordmark">
    <span class="wordmark__square"></span>
    <span class="wordmark__name">Dunewood Real Estate</span>
  </div>

  <div class="back__contact-panel"></div>
  <div class="back__agent-photo" role="img" aria-label="Portrait photo of the sales agent"></div>

  <h2 class="back__agent-name">Agent Name</h2>
  <div class="back__rule back__rule--top"></div>
  <div class="back__phone">
    <svg viewBox="0 0 40 40" aria-hidden="true">
      <circle cx="20" cy="20" r="17" fill="none" stroke="currentColor" stroke-width="3"/>
      <path d="M14 11c1-1 2.5-1 3 0l2 4c.4.9 0 1.8-.8 2.3l-1.3.8c.9 2.3 2.6 4.2 4.8 5.3l.9-1.2c.6-.8 1.5-1 2.3-.6l3.8 2.1c.9.5 1 1.9.1 2.8l-1.4 1.4c-1.3 1.3-3.3 1.6-5 .8-4.6-2.2-8.1-5.9-10-10.6-.7-1.7-.3-3.6 1-4.9z" fill="currentColor"/>
    </svg>
    <span>03 9012 4470</span>
  </div>
  <div class="back__rule back__rule--bottom"></div>
  <p class="back__online">Info@DunewoodRealEstate.com.au<br>www.dunewoodrealestate.com.au</p>

  <svg class="back__divider" viewBox="0 0 294 18" aria-hidden="true">
    <line x1="0" y1="12" x2="117" y2="12" stroke="#c62128" stroke-width="1.5"/>
    <line x1="177" y1="12" x2="294" y2="12" stroke="#c62128" stroke-width="1.5"/>
    <path d="M147 1a5 5 0 0 0-5 5c0 3.5 5 9 5 9s5-5.5 5-9a5 5 0 0 0-5-5z" fill="none" stroke="#c62128" stroke-width="1.5"/>
    <circle cx="147" cy="6" r="1.8" fill="#c62128"/>
  </svg>

  <div class="office office--head">
    <p class="office__label">Head Office</p>
    <p class="office__address">14/6 Horizon Way, Laverton, VIC 3028</p>
  </div>
  <div class="office office--branch">
    <p class="office__label">Branch Office</p>
    <p class="office__address">92 Station Rd, Reservoir, VIC 3073</p>
  </div>
</section>

</body>
</html>
```